Quillmark Solutions - Website for a CRM IT Services Provider to Non-profits

We need a website design for our company that provides IT services to non-profits to enable them to manage their donors and philanthropy within their organization.

We would like to see a design that uses the colors in our logo and a funky take on how to uniquely present a topic as boring as IT. Examples of sites that we really like: brantwickdale.com, www.marlowpetrie.com, tinwhistlebox.com

The final design should communicate that we are a professional, yet creative company that is fun to work with.

Target Market(s)

Non-profits who tend to be young, creative types that are low-tech

Industry/Entity Type

It Company

Requirements
Must have
• Must include tabs for Home, Contact Us, About, Projects, and Blog. The site must use the logo we have attached on all of the page, in one way or another (it can be small & in the corner).

The site has to work on all mobile browsers (iphone, ipad).
Nice to have
• It would be great if I could supply some HTML for the Contact page that would allow me to capture leads and put them directly into my CRM application. It's very easy to set up.
Should not have
• The design should not use old-style fonts and should not have a lot of dark colors. Keep it similar to our logo, clean and simple. We're not looking for a busy home page.

```html
<!DOCTYPE html>
<html lang="en">
<head>
<meta charset="utf-8">
<title>Quillmark Solutions</title>
<link rel="stylesheet" href="https://fonts.googleapis.com/css2?family=Cabin+Sketch:wght@400;700&family=Questrial&display=swap">
<style>
  :root {
    --red: #b04848;
    --green: #4ab546;
    --blue: #4a7db5;
    --brown: #b07748;
    --grey-text: #555555;
    --logo-grey: #7a7a7a;
    --frame: #bfd2dc;
    --white: #ffffff;
  }
  html, body {
    margin: 0;
    padding: 0;
    width: 988px;
    height: 1200px;
    overflow: hidden;
    background: var(--white);
  }
  .page {
    position: relative;
    width: 1020px;
    height: 1239px;
    transform: scale(0.9686);
    transform-origin: 0 0;
    font-family: "Cabin Sketch", cursive;
    color: var(--white);
  }
  .abs { position: absolute; }

  /* header */
  .site-header {
    left: 40px; top: 5px; width: 938px; height: 148px;
    border: 1px solid var(--frame);
    box-sizing: border-box;
  }
  .brand-mark {
    left: 53px; top: 17px; width: 126px; height: 126px;
    border-radius: 50%;
    background: var(--blue);
  }
  .brand-name {
    left: 200px; top: 42px;
    font-family: "Questrial", sans-serif;
    font-size: 46px;
    line-height: 1;
    color: var(--logo-grey);
    margin: 0;
    font-weight: 400;
  }
  .brand-name span {
    display: block;
    font-size: 17px;
    letter-spacing: 4px;
    text-align: right;
    margin-top: 8px;
  }
  .account-links {
    right: 57px; top: 16px;
    font-family: "Questrial", sans-serif;
    font-size: 11px;
    color: var(--grey-text);
    letter-spacing: .3px;
  }
  .follow-label {
    left: 710px; top: 78px;
    font-family: "Questrial", sans-serif;
    font-size: 10px;
    color: var(--grey-text);
  }
  .follow-rule {
    left: 600px; top: 90px; width: 105px; height: 1px;
    background: #e4e4e4;
  }
  .social-list { left: 761px; top: 40px; display: flex; gap: 4px; margin: 0; padding: 0; list-style: none; }
  .social-list li {
    width: 48px; height: 48px;
    border: 1px solid #d6d6d6;
    box-sizing: border-box;
    background: #f4f7f9;
  }
  .search-box {
    left: 745px; top: 116px; width: 220px; height: 21px;
    border: 1px solid #d0d0d0;
    box-sizing: border-box;
    font-family: "Questrial", sans-serif;
    font-size: 11px;
    color: #777;
    padding: 3px 7px;
  }
  .search-glass {
    left: 870px; top: 80px; width: 122px; height: 122px;
    border-radius: 50%;
    background: radial-gradient(circle at 40% 35%, #e2eefc 0%, #9cc3f0 55%, #3d3d3d 100%);
  }

  /* navigation */
  .main-nav { left: 40px; top: 172px; width: 940px; height: 40px; }
  .main-nav a {
    position: absolute; top: 0; width: 220px; height: 40px;
    font-size: 34px; line-height: 38px; text-align: center;
    color: var(--white); text-decoration: none; letter-spacing: 1px;
  }
  .nav-about { left: 0; background: var(--red); }
  .nav-projects { left: 240px; background: var(--green); }
  .nav-blog { left: 480px; background: var(--blue); }
  .nav-contact { left: 720px; background: var(--brown); }

  /* feature panels */
  .panel { width: 540px; height: 280px; }
  .panel h2 {
    position: absolute; margin: 0;
    font-size: 92px; font-weight: 700; line-height: 1; letter-spacing: 1px;
  }
  .panel p {
    position: absolute; margin: 0;
    font-size: 18px; line-height: 29px; letter-spacing: 1.2px;
  }
  .more {
    position: absolute;
    font-size: 21px; letter-spacing: 1.5px; text-decoration: none; color: var(--white);
  }
  .arrow { position: absolute; width: 108px; height: 70px; }

  .panel-about { left: 40px; top: 229px; background: var(--red); }
  .panel-about h2 { left: 20px; top: 12px; }
  .panel-about p { left: 40px; top: 106px; }
  .panel-about .more { left: 232px; top: 218px; }
  .panel-about .arrow { left: 398px; top: 197px; }

  .panel-projects { left: 440px; top: 526px; background: var(--green); }
  .panel-projects h2 { right: 20px; top: 12px; }
  .panel-projects p { right: 40px; top: 104px; text-align: right; }
  .panel-projects .more { left: 233px; top: 218px; }
  .panel-projects .arrow { left: 398px; top: 197px; }

  .panel-blog { left: 40px; top: 823px; background: var(--blue); }
  .panel-blog h2 { left: 18px; top: 8px; }
  .panel-blog p { left: 40px; top: 106px; }
  .panel-blog .more { left: 232px; top: 218px; }
  .panel-blog .arrow { left: 398px; top: 197px; }

  .panel-contact { left: 40px; top: 1119px; width: 940px; height: 100px; background: var(--brown); }
  .panel-contact h2 { left: 18px; top: 10px; }
  .panel-contact p { left: 392px; top: 20px; }
  .panel-contact .more { left: 632px; top: 36px; }
  .panel-contact .arrow { left: 798px; top: 14px; }

  /* artwork areas */
  .art-icons {
    left: 690px; top: 229px; width: 196px; height: 280px;
    background: linear-gradient(180deg, #f5a2b4 0%, #5cc6ea 40%, #62b9f0 60%, #f4c53c 100%);
    border-radius: 40px 40px 20px 20px;
  }
  .art-maker {
    left: 80px; top: 535px; width: 296px; height: 262px;
    background: linear-gradient(180deg, #f3efe6 0%, #e8d9a8 60%, #e0c38a 100%);
    border-radius: 8px;
  }
  .art-chat {
    left: 600px; top: 823px; width: 380px; height: 280px;
    background: linear-gradient(135deg, #35c5ec 0%, #88cf30 40%, #ffd23a 70%, #ef2a8a 100%);
  }
</style>
</head>
<body>
<div class="page">

  <header class="site-header abs"></header>
  <div class="brand-mark abs"></div>
  <h1 class="brand-name abs">Quillmark<span>SOLUTIONS</span></h1>
  <div class="account-links abs">You are not logged in &nbsp;|&nbsp; Login or Register</div>
  <div class="follow-rule abs"></div>
  <div class="follow-label abs">Follow us</div>
  <ul class="social-list abs">
    <li></li><li></li><li></li><li></li>
  </ul>
  <div class="search-box abs">Search our site</div>
  <div class="search-glass abs" role="img" aria-label="Magnifying glass illustration"></div>

  <nav class="main-nav abs">
    <a class="nav-about" href="#about">about</a>
    <a class="nav-projects" href="#projects">projects</a>
    <a class="nav-blog" href="#blog">blog</a>
    <a class="nav-contact" href="#contact">contact</a>
  </nav>

  <section class="panel panel-about abs" id="about">
    <h2>about</h2>
    <p>lorem ipsum dolor sit amet consectetur<br>adipisicing elit sed do eiusmod tempor<br>incididunt ut labore et dolore magna aliqua</p>
    <a class="more" href="#about">click for more</a>
    <svg class="arrow" viewBox="0 0 108 70"><path d="M3 24 L62 26 L60 3 L105 36 L62 67 L62 46 L4 47 Z" fill="none" stroke="#fff" stroke-width="4" stroke-linejoin="round"/></svg>
  </section>
  <div class="art-icons abs" role="img" aria-label="Colourful collage of technology and communication icons"></div>

  <div class="art-maker abs" role="img" aria-label="Cartoon of a smiling crafter holding a crayon beside scissors and glue"></div>
  <section class="panel panel-projects abs" id="projects">
    <h2>projects</h2>
    <p>lorem ipsum dolor sit amet consectetur<br>adipisicing elit sed do eiusmod tempor<br>incididunt ut labore et dolore magna aliqua</p>
    <a class="more" href="#projects">click for more</a>
    <svg class="arrow" viewBox="0 0 108 70"><path d="M3 24 L62 26 L60 3 L105 36 L62 67 L62 46 L4 47 Z" fill="none" stroke="#fff" stroke-width="4" stroke-linejoin="round"/></svg>
  </section>

  <section class="panel panel-blog abs" id="blog">
    <h2>blog</h2>
    <p>lorem ipsum dolor sit amet consectetur<br>adipisicing elit sed do eiusmod tempor<br>incididunt ut labore et dolore magna aliqua</p>
    <a class="more" href="#blog">click for more</a>
    <svg class="arrow" viewBox="0 0 108 70"><path d="M3 24 L62 26 L60 3 L105 36 L62 67 L62 46 L4 47 Z" fill="none" stroke="#fff" stroke-width="4" stroke-linejoin="round"/></svg>
  </section>
  <div class="art-chat abs" role="img" aria-label="Laptop surrounded by colourful speech bubbles"></div>

  <section class="panel panel-contact abs" id="contact">
    <h2>contact</h2>
    <p>lorem ipsum dolor sit<br>amet consectetur</p>
    <a class="more" href="#contact">click for more</a>
    <svg class="arrow" viewBox="0 0 108 70"><path d="M3 24 L62 26 L60 3 L105 36 L62 67 L62 46 L4 47 Z" fill="none" stroke="#fff" stroke-width="4" stroke-linejoin="round"/></svg>
  </section>

</div>
</body>
</html>
```